Create Direct Mail Flyer For House Painting Company

The flyer needs to promote "Free Cheese Every Month" (When they paint their whole house. We want to Focus on the offer, also a free colour consultation, the awards and the guarantees! This will be a full colour 2 sided letter box drop flyer.
This is an emotional Direct Response flyer. I want the Headline to be Bold and stand out. Follow the branding if the website https://larkfieldresidencecraft.com.au/
I have attached some social media photos to show you the promotion idea of free cheese every month. Use better photos if you have them.
I have given you a number of photos to use on the brochure, use your skills to determine what you feel is best to use. Also with the Colour consultation points use small photos to emphasise the points.
Have the testimonials and the team photo on the back.
Also have urgency. ACT NOW -OFFER ENDING SOON!

Target Market(s)

Home Owners

Industry/Entity Type

House Painting, Roof Painting

Colors
0054AA
0677BA
7BADD7
CADEEF
E8F1F8

Requirements
Must have
• Keep the Brand Colours. I have attached a sample flyer that shows a concept that I like. Have the testimonials on the back of the flyer. I do not want the flyer to look to busy.

```html
<!DOCTYPE html>
<html lang="en">
<head>
<meta charset="utf-8">
<title>Larkfield Residence Craft – Flyer</title>
<link href="https://fonts.googleapis.com/css2?family=Montserrat:wght@400;600;700;800;900&family=Open+Sans:wght@400;600&display=swap" rel="stylesheet">
<style>
  :root{
    --brand-deep:#0054AA;
    --brand:#0677BA;
    --brand-mid:#7BADD7;
    --brand-light:#CADEEF;
    --brand-pale:#E8F1F8;
    --ink:#1e2a36;
    --charcoal:#3a4048;
    --stage:#e6e8eb;
    --white:#ffffff;
    --star:#f2b01e;
  }
  *{box-sizing:border-box;margin:0;padding:0}
  html,body{width:802px;height:1200px;overflow:hidden}
  body{background:var(--stage);font-family:"Open Sans",Arial,sans-serif;color:var(--ink);position:relative}
  .page{position:absolute;top:331px;width:380px;height:537px;background:var(--white);overflow:hidden;box-shadow:0 4px 14px rgba(0,0,0,.18)}
  .page--front{left:14px}
  .page--back{left:408px}
  .brand{display:flex;align-items:center;gap:5px;font-family:"Montserrat",sans-serif;font-weight:800;font-size:11px;letter-spacing:.5px;text-transform:uppercase}
  .brand__mark{width:10px;height:10px;background:currentColor}
  .photo{display:block}

  /* front */
  .hero{position:absolute;left:0;top:0;width:380px;height:120px;background:linear-gradient(160deg,#a9c3d8,#6f8797 60%,#4b5a63)}
  .hero .brand{position:absolute;left:8px;top:44px;color:var(--brand-deep);background:var(--white);padding:5px 7px}
  .hero__tag{position:absolute;right:10px;top:10px;width:150px;font-family:"Montserrat",sans-serif;font-weight:800;font-size:9px;line-height:1.2;color:var(--white);text-transform:uppercase;text-align:center;background:var(--brand-deep);padding:5px}
  .pitch{position:absolute;left:0;top:120px;width:170px;height:375px;background:var(--charcoal);color:var(--white);padding:14px 10px}
  .pitch__headline{font-family:"Montserrat",sans-serif;font-weight:900;font-size:17px;line-height:1.12;text-transform:uppercase}
  .pitch__headline em{font-style:normal;color:var(--brand-mid)}
  .pitch__body{font-size:7.5px;line-height:1.4;margin-top:9px;color:#dfe6ec}
  .pitch__sub{font-family:"Montserrat",sans-serif;font-weight:800;font-size:8.5px;text-transform:uppercase;margin:12px 0 5px}
  .services{display:flex;gap:4px}
  .service{flex:1;text-align:center;font-size:6px}
  .service .photo{height:36px;margin-bottom:3px}
  .s1{background:linear-gradient(135deg,#c9b89a,#7d8e9c)}
  .s2{background:linear-gradient(135deg,#8a5a44,#5b6b78)}
  .s3{background:linear-gradient(135deg,#d9c7a7,#a89274)}
  .guarantees{display:grid;grid-template-columns:1fr 1fr;gap:5px 6px}
  .guarantee{display:flex;align-items:center;gap:4px;font-size:6.5px;font-weight:600}
  .guarantee__badge{width:18px;height:18px;border-radius:50%;background:var(--white);border:2px solid var(--brand-mid);flex:none}
  .steps{position:absolute;left:170px;top:120px;width:210px;height:375px;background:var(--brand-pale);padding:8px 8px}
  .steps__title{font-family:"Montserrat",sans-serif;font-weight:800;font-size:8.5px;line-height:1.2;color:var(--brand-deep);text-transform:uppercase;margin-bottom:6px}
  .step{display:flex;gap:5px;background:var(--brand);color:var(--white);margin-bottom:6px;height:77px;padding:5px}
  .step:nth-child(even){background:var(--brand-deep)}
  .step__num{font-family:"Montserrat",sans-serif;font-weight:900;font-size:22px;line-height:1;width:16px;flex:none}
  .step__text h3{font-family:"Montserrat",sans-serif;font-size:7.5px;font-weight:800;text-transform:uppercase;margin-bottom:3px}
  .step__text p{font-size:6.5px;line-height:1.35}
  .step .photo{width:52px;flex:none;background:linear-gradient(135deg,var(--brand-light),#9aa9b4)}
  .callbar{position:absolute;left:0;bottom:0;width:380px;height:42px;background:var(--white);border-top:3px solid var(--brand-deep);display:flex;align-items:center;justify-content:space-between;padding:0 12px}
  .callbar__label{font-family:"Montserrat",sans-serif;font-weight:800;font-size:13px;color:var(--brand-deep)}
  .callbar__phone{display:flex;align-items:center;gap:5px;font-family:"Montserrat",sans-serif;font-weight:800;font-size:15px;color:var(--brand-deep)}
  .callbar__web{font-size:6.5px;color:var(--charcoal)}

  /* back */
  .back-head{position:absolute;left:0;top:0;width:380px;height:112px;background:linear-gradient(180deg,var(--brand-deep),var(--brand));color:var(--white);text-align:center}
  .back-head .brand{justify-content:center;padding-top:18px;font-size:13px}
  .back-head h1{font-family:"Montserrat",sans-serif;font-weight:900;font-size:26px;letter-spacing:1px;margin-top:16px}
  .reviews{position:absolute;left:10px;top:122px;width:360px;display:grid;grid-template-columns:1fr 1fr;gap:9px}
  .review{position:relative;background:var(--brand-pale);padding:9px 9px 9px 22px;height:170px;border-left:3px solid var(--brand)}
  .review__quote{position:absolute;left:5px;top:4px;font-family:"Montserrat",sans-serif;font-weight:900;font-size:22px;color:var(--brand)}
  .review__name{font-family:"Montserrat",sans-serif;font-weight:700;font-size:8px;color:var(--brand-deep)}
  .review__stars{color:var(--star);font-size:8px;letter-spacing:1px;margin:2px 0 5px}
  .review p{font-size:6.8px;line-height:1.45;color:var(--charcoal)}
  .back-foot{position:absolute;left:0;bottom:0;width:380px;height:50px;background:var(--brand-deep);color:var(--white);display:flex;align-items:center;justify-content:space-between;padding:0 12px}
  .back-foot .callbar__label,.back-foot .callbar__phone{color:var(--white)}
  .back-foot__contact{font-size:6.5px;line-height:1.6;text-align:right}
</style>
</head>
<body>

<section class="page page--front">
  <div class="hero photo" role="img" aria-label="Freshly painted two-storey family home">
    <div class="brand"><span class="brand__mark"></span>Larkfield Residence Craft</div>
    <div class="hero__tag">Book your free colour consultation while this offer lasts!</div>
  </div>

  <div class="pitch">
    <h2 class="pitch__headline">Transform your home &amp; enjoy <em>free cheese every month!</em></h2>
    <p class="pitch__body">Paint your whole house with us and we will deliver a generous cheese hamper to your door every month for a full year. Act now – offer ending soon!</p>
    <h3 class="pitch__sub">Our services</h3>
    <div class="services">
      <div class="service"><div class="photo s1" role="img" aria-label="Exterior house painting"></div>House Painting</div>
      <div class="service"><div class="photo s2" role="img" aria-label="Roof painting"></div>Roof Painting</div>
      <div class="service"><div class="photo s3" role="img" aria-label="Colour consultation swatches"></div>Colour Consult</div>
    </div>
    <h3 class="pitch__sub">Our guarantees</h3>
    <div class="guarantees">
      <div class="guarantee"><span class="guarantee__badge"></span>5 Year Warranty</div>
      <div class="guarantee"><span class="guarantee__badge"></span>On Time Finish</div>
      <div class="guarantee"><span class="guarantee__badge"></span>Clean Site</div>
      <div class="guarantee"><span class="guarantee__badge"></span>Fixed Price</div>
    </div>
  </div>

  <div class="steps">
    <h2 class="steps__title">It is important to select the correct colours for your home</h2>
    <div class="step"><span class="step__num">1</span><div class="step__text"><h3>Consider the room's purpose</h3><p>Think about how each space is used and the feeling you want to create.</p></div><div class="photo" role="img" aria-label="Bright living room interior"></div></div>
    <div class="step"><span class="step__num">2</span><div class="step__text"><h3>Look at natural light</h3><p>Light changes every shade, so test colours at different times of the day.</p></div><div class="photo" role="img" aria-label="Sunlit window and wall"></div></div>
    <div class="step"><span class="step__num">3</span><div class="step__text"><h3>Match your surroundings</h3><p>Roof, garden and street all shape which tones will suit your home best.</p></div><div class="photo" role="img" aria-label="House facade with garden"></div></div>
    <div class="step"><span class="step__num">4</span><div class="step__text"><h3>Ask the experts</h3><p>Our consultant visits free of charge and guides you to a confident choice.</p></div><div class="photo" role="img" aria-label="Consultant holding colour chart"></div></div>
  </div>

  <div class="callbar">
    <span class="callbar__label">Call Us Now</span>
    <span class="callbar__phone">
      <svg width="14" height="14" viewBox="0 0 24 24" aria-hidden="true"><path fill="currentColor" d="M6.6 10.8a15.1 15.1 0 0 0 6.6 6.6l2.2-2.2c.3-.3.7-.4 1-.2 1.1.4 2.3.6 3.6.6.6 0 1 .4 1 1V20c0 .6-.4 1-1 1A17 17 0 0 1 3 4c0-.6.4-1 1-1h3.5c.6 0 1 .4 1 1 0 1.3.2 2.5.6 3.6.1.3 0 .7-.2 1z"/></svg>
      1300 555 217
    </span>
    <span class="callbar__web">larkfieldresidencecraft.com.au</span>
  </div>
</section>

<section class="page page--back">
  <header class="back-head">
    <div class="brand"><span class="brand__mark"></span>Larkfield Residence Craft</div>
    <h1>TESTIMONIALS</h1>
  </header>

  <div class="reviews">
    <article class="review"><span class="review__quote">“</span><div class="review__name">Dale Fenwick</div><div class="review__stars">★★★★★</div><p>The team was on time every day and left the site spotless. Our weatherboard home looks brand new and the colour advice was spot on. Highly recommended.</p></article>
    <article class="review"><span class="review__quote">“</span><div class="review__name">Mara Oakes</div><div class="review__stars">★★★★★</div><p>From the first quote to the final walkthrough everything was clear and friendly. The roof and trims came up beautifully and the neighbours keep asking who did it.</p></article>
    <article class="review"><span class="review__quote">“</span><div class="review__name">Trevor L</div><div class="review__stars">★★★★★</div><p>Professional painters who actually listen. They prepared every surface properly, kept us updated and finished a day early. We will use them again for the interior.</p></article>
    <article class="review"><span class="review__quote">“</span><div class="review__name">Priya Vandermeer</div><div class="review__stars">★★★★★</div><p>The free colour consultation made choosing so easy. The crew were polite, tidy and careful with our garden. The result is better than we imagined.</p></article>
  </div>

  <footer class="back-foot">
    <div>
      <div class="callbar__label">Call Us Now</div>
      <div class="callbar__phone">1300 555 217</div>
    </div>
    <div class="back-foot__contact">hello@larkfieldresidencecraft.com.au<br>larkfieldresidencecraft.com.au</div>
  </footer>
</section>

</body>
</html>
```